BRWN Coaching Website

I would like someone to design my website. I have an existing site which is really basic and needs an overhaul. I have attached a powerpoint with all the information I require. I am flexible with the design and layout and am ok with graphics being added to enhance the attractiveness of the site.

```html
<!DOCTYPE html>
<html lang="en">
<head>
<meta charset="utf-8">
<title>BRWN Coaching</title>
<link rel="stylesheet" href="https://fonts.googleapis.com/css2?family=Oxygen:wght@300;400&display=swap">
<style>
  :root {
    --orange: #f05a28;
    --orange-soft: #f2794a;
    --blue: #1f6fb8;
    --nav-top: #3a92d4;
    --nav-bottom: #0e4c9b;
    --text: #444444;
    --muted: #7a7a7a;
    --footer-top: #f1f1f1;
    --footer-bottom: #fbfbfb;
    --line: #e6e6e6;
    --card-btn: #f3f3f3;
    --photo-top: #8a8a84;
    --photo-bottom: #c9b6a4;
    --white: #ffffff;
  }
  * { margin: 0; padding: 0; box-sizing: border-box; }
  html, body { width: 1200px; height: 607px; overflow: hidden; background: var(--white); }
  body { position: relative; font-family: "Oxygen", sans-serif; color: var(--text); }

  .brand { position: absolute; left: 60px; top: 42px; display: flex; align-items: center; gap: 12px; }
  .brand-mark { width: 26px; height: 26px; background: var(--orange); }
  .brand-name { font-size: 38px; font-weight: 400; color: var(--blue); letter-spacing: 0.5px; }

  .contact { position: absolute; right: 76px; top: 52px; text-align: right; }
  .contact-phone { font-size: 30px; color: var(--orange); font-weight: 400; line-height: 1.2; }
  .contact-email { display: block; font-size: 16.5px; color: var(--blue); text-decoration: none; margin-top: 4px; }

  .main-nav {
    position: absolute; left: 57px; top: 199px; width: 286px; height: 245px;
    background: linear-gradient(to bottom, var(--nav-top), var(--nav-bottom));
    border-radius: 3px; padding: 16px 24px 0 24px;
  }
  .main-nav ul { list-style: none; }
  .main-nav li { border-bottom: 1px solid rgba(255,255,255,0.22); }
  .main-nav li:last-child { border-bottom: none; }
  .main-nav a { display: block; color: var(--white); text-decoration: none; font-size: 17.5px; padding: 0 18px; line-height: 53px; }

  .intro { position: absolute; left: 377px; top: 204px; width: 530px; }
  .intro-title { font-size: 27.5px; font-weight: 400; color: var(--orange); margin-bottom: 8px; }
  .intro p { font-size: 15.8px; line-height: 26.5px; margin-bottom: 5px; }
  .intro-cta { position: absolute; top: 218px; left: 1px; font-size: 17.5px; color: var(--orange-soft); text-decoration: none; white-space: nowrap; }

  .profile-card { position: absolute; left: 938px; top: 200px; width: 205px; height: 265px; border-radius: 3px; overflow: hidden; border: 1px solid #d8d8d8; }
  .profile-photo { height: 220px; background: linear-gradient(160deg, var(--photo-top), var(--photo-bottom)); }
  .profile-link { display: block; height: 44px; background: var(--card-btn); text-align: center; line-height: 44px; font-size: 17.5px; color: var(--text); text-decoration: none; border-top: 1px solid #d8d8d8; }

  .site-footer {
    position: absolute; left: 0; top: 509px; width: 1200px; height: 98px;
    background: linear-gradient(to bottom, var(--footer-top), var(--footer-bottom));
    border-top: 1px solid var(--line);
  }
  .footer-note { position: absolute; left: 60px; top: 32px; font-size: 13.5px; color: var(--muted); }
  .social { position: absolute; left: 1015px; top: 28px; display: flex; gap: 10px; list-style: none; }
  .social li { width: 24px; height: 24px; border-radius: 2px; }
  .social .s1 { background: #3b5998; }
  .social .s2 { background: #4fc3ee; }
  .social .s3 { background: #1c74b3; }
  .social .s4 { background: #f5871f; }
</style>
</head>
<body>
  <header>
    <div class="brand">
      <span class="brand-mark"></span>
      <span class="brand-name">BRWN Coaching</span>
    </div>
    <div class="contact">
      <div class="contact-phone">1300 555 017</div>
      <a class="contact-email" href="#">Maren.Hale@brwncoaching.com</a>
    </div>
  </header>

  <nav class="main-nav">
    <ul>
      <li><a href="#">Invididula Coaching (1)</a></li>
      <li><a href="#">Group Work (2)</a></li>
      <li><a href="#">Resources (3)</a></li>
      <li><a href="#">Inspiration Booth (5)</a></li>
    </ul>
  </nav>

  <main class="intro">
    <h1 class="intro-title">Welcome to BRWN Coaching Website</h1>
    <p>Welcome to BRWN Coaching where we put a new prespective on the way you work, live and play.</p>
    <p>Through our programs you will learn new skills &amp; techniques to enable you to break through the barriers that have kept you from reaching your full potential up to now.</p>
    <a class="intro-cta" href="#">Get your free 30 minute introductory coaching session (4)</a>
  </main>

  <aside class="profile-card">
    <div class="profile-photo" role="img" aria-label="Portrait photo of the coach"></div>
    <a class="profile-link" href="#">About Maren (6)</a>
  </aside>

  <footer class="site-footer">
    <p class="footer-note">© 2014 Company Name&nbsp; All right reserved&nbsp; Term of Use</p>
    <ul class="social" aria-label="Social links">
      <li class="s1"></li>
      <li class="s2"></li>
      <li class="s3"></li>
      <li class="s4"></li>
    </ul>
  </footer>
</body>
</html>
```